Business Card Design

Hello,
I try and keep my business card fresh and current. So about every year i get a new one. This year I'd like something with a white background and black lettering.
Before you start - I do not want my phone number or any other description on the card other than my url and my email.

I'd like a double sided business card with
TobFarnsby.com on one side

and

Tob@TobFarnsby.com on the other side of the card

Thinking very minimalistic and modern.
I don't have a particular font i mind or how to capitalize my name or website. This card will lead people to my new website that is being designed to showcase my photography and music.

* Initial thought was the front side of the card having a grid-like pattern built out of dashes or periods, with my website sitting within the pattern and on the back side my email on a stark white background. But that might look completely lame - haha.

I'm looking forward to seeing what you come up with.

thank you,
- tob farnsby

Reason: Want to spend some more time with the designs and add a little $. thanks for all the designs - tob

Wanted to add a little $ and spend some more time with the designs.

big thanks to all who have submitted work 

- tob

Industry/Entity Type

Business

Contact Information for Business Card

www.tobfarnsby.com
tob@tobfarnsby.com

Colors
000000
ffffff

Requirements
Must have
• tobfarnsby.com
tob@tobfarnsby.com
Should not have
• phone number
any description of what i do, photography or music

```html
<!DOCTYPE html>
<html lang="en">
<head>
<meta charset="utf-8">
<title>TobFarnsby.com — Business Card</title>
<link rel="stylesheet" href="https://fonts.googleapis.com/css2?family=Jost:wght@300&display=swap">
<style>
  :root {
    --stage-center: #2b2d2e;
    --stage-edge: #050606;
    --tile-light: #dfe3e2;
    --tile-mid: #c6cbca;
    --tile-shadow: #a2a8a7;
    --band: #1e1f1f;
    --band-edge: #0d0d0d;
    --type: #e9ecec;
  }
  html, body {
    margin: 0;
    width: 1200px;
    height: 900px;
    overflow: hidden;
  }
  body {
    position: relative;
    background: radial-gradient(ellipse 55% 60% at 50% 50%, var(--stage-center), var(--stage-edge));
    font-family: "Jost", "Futura", sans-serif;
    font-weight: 300;
  }
  .card {
    position: absolute;
    overflow: hidden;
  }
  .card--front { left: 296px; top: 59px; width: 608px; height: 355px; }
  .card--back  { left: 296px; top: 481px; width: 610px; height: 356px; }
  .card__texture {
    position: absolute;
    inset: 0;
    background:
      radial-gradient(ellipse 70% 60% at 45% 40%, var(--tile-light), transparent 75%),
      linear-gradient(180deg, var(--tile-mid), var(--tile-light) 45%, var(--tile-mid) 80%, var(--tile-shadow));
  }
  .band {
    position: absolute;
    left: 28px;
    right: 28px;
    top: 157px;
    height: 36px;
    background: var(--band);
    box-shadow: 0 2px 6px rgba(0,0,0,.45);
    clip-path: polygon(0 50%, 12px 0, calc(100% - 12px) 0, 100% 50%, calc(100% - 12px) 100%, 12px 100%);
  }
  .band__text {
    position: absolute;
    left: 0;
    right: 0;
    top: 157px;
    margin: 0;
    text-align: center;
    color: var(--type);
    font-size: 24px;
    font-weight: 300;
    line-height: 36px;
    letter-spacing: 27px;
    padding-left: 27px;
    white-space: nowrap;
  }
  .email-cluster {
    position: absolute;
    left: 0;
    top: 0;
    width: 610px;
    height: 200px;
  }
  .email-cluster__hex {
    fill: var(--band);
    stroke: var(--band-edge);
    stroke-width: 1;
  }
  .email-cluster__stem { fill: var(--band); }
  .email-cluster__letter {
    fill: var(--type);
    font-family: "Jost", "Futura", sans-serif;
    font-weight: 300;
    font-size: 24px;
  }
  .email-cluster__at { font-size: 30px; }
</style>
</head>
<body>
  <section class="card card--front">
    <div class="card__texture" role="img" aria-label="White raised hexagon tile relief texture"></div>
    <div class="band"></div>
    <p class="band__text">TobFarnsby.com</p>
  </section>

  <section class="card card--back" aria-label="Tob@TobFarnsby.com">
    <div class="card__texture" role="img" aria-label="White raised hexagon tile relief texture"></div>
    <div class="band"></div>
    <svg class="email-cluster" viewBox="0 0 610 200">
      <rect class="email-cluster__stem" x="287" y="130" width="32" height="30"/>
      <polygon class="email-cluster__hex" points="261,49 282,60.5 282,83.5 261,95 240,83.5 240,60.5"/>
      <polygon class="email-cluster__hex" points="303,49 324,60.5 324,83.5 303,95 282,83.5 282,60.5"/>
      <polygon class="email-cluster__hex" points="345,49 366,60.5 366,83.5 345,95 324,83.5 324,60.5"/>
      <polygon class="email-cluster__hex" points="303,94 324,105.5 324,128.5 303,140 282,128.5 282,105.5"/>
      <text class="email-cluster__letter" x="261" y="81" text-anchor="middle">T</text>
      <text class="email-cluster__letter" x="303" y="81" text-anchor="middle">o</text>
      <text class="email-cluster__letter" x="345" y="81" text-anchor="middle">b</text>
      <text class="email-cluster__letter email-cluster__at" x="303" y="127" text-anchor="middle">@</text>
    </svg>
    <p class="band__text">TobFarnsby.com</p>
  </section>
</body>
</html>
```